Single Page/Scrolling Design for Model Recruitment site

We need a design (and if you are capable, coding) for our company, Vero Parlour Room (LA as in Los Angeles). We like modern single page designs, hence the title for the project. We have already had a designer come up with a logo, which is attached. You're free to play around with the colors, although we want the site to have a feminine appeal to it.

The site is basically a recruitment project for girls who are interested in working as chat hosts for cam sites. We don't want anything cheesy that feels like a porn site. The inspiration for the logo (and the inspiration for the site) comes from the French and English salons of the late 18th century, where beautiful and intelligent women would gather to discuss a range of topics. We want the website to convey that this work is fun and exciting. Please keep these things in mind for the design.

As I mentioned, we like the modern look and feel of single page designs, especially because we don't have a ton of content. We just need an "About us" area, a "Work from Home" area, a "Work at The Parlour Room" area, and "Contact Us" area which should have text boxes for entering email, subject, a message, etc.

The logo I mentioned is attached, as well as a very crude mockup of the layout of all the content I described.

Target Market(s)

Women age 18-35.

Industry/Entity Type

It Company

Font styles to use
Serif
Decorative
Script

Colors

Designer to choose colors to be used in the design.

Requirements
Should not have
• Images that are super sexual or even slightly pornographic. We want this to appeal to a broad range of women.

```html
<!DOCTYPE html>
<html lang="en">
<head>
<meta charset="utf-8">
<title>Vero Parlour Room</title>
<link href="https://fonts.googleapis.com/css2?family=Montserrat:wght@400;600;700&family=Open+Sans:wght@400;600;700&display=swap" rel="stylesheet">
<style>
:root{
  --magenta:#c8157f;
  --magenta-light:#e42a9c;
  --magenta-dark:#9e0c66;
  --ink:#4a4a4a;
  --ink-soft:#777;
  --hero-bg:#efefef;
  --band-bg:#ececec;
  --white:#fff;
  --dark:#262626;
  --darker:#1e1e1e;
  --line-dark:#3a3a3a;
  --field:#fff;
}
*{box-sizing:border-box;margin:0;padding:0}
html,body{width:1200px;height:2362px;overflow:hidden}
body{font-family:"Open Sans",Arial,sans-serif;color:var(--ink);background:var(--white);position:relative}
.abs{position:absolute}
h1,h2,h3,h4{font-family:"Montserrat",Arial,sans-serif}

/* nav */
.topbar{left:0;top:0;width:1200px;height:47px;background:linear-gradient(var(--magenta-light),var(--magenta-dark))}
.nav{left:214px;top:9px;display:flex;gap:6px}
.nav a{color:#fff;text-decoration:none;font:400 14px "Open Sans",sans-serif;padding:6px 10px;border-radius:4px}
.nav a.active{background:#5a0a3c}
.phone-pill{left:846px;top:9px;width:130px;height:28px;border-radius:6px;background:#5a0a3c;color:#fff;font-size:13px;display:flex;align-items:center;justify-content:center;gap:8px}

/* hero */
.hero{left:0;top:47px;width:1200px;height:421px;background:var(--hero-bg)}
.hero-logo{left:222px;top:147px;width:226px;height:226px;border-radius:50%;background:#fff;border:8px solid var(--magenta);display:flex;align-items:center;justify-content:center;gap:12px;flex-direction:column;text-align:center}
.hero-logo span{font:700 17px/1.2 "Montserrat",sans-serif;color:var(--magenta);width:170px}
.hero-logo i{width:70px;height:70px;border-radius:50%;background:var(--magenta);display:block}
.arrow{width:44px;height:44px;border-radius:50%;border:3px solid var(--magenta);top:238px;display:flex;align-items:center;justify-content:center;background:#fff}
.hero-title{left:560px;top:160px;font:700 58px/1 "Montserrat",sans-serif;color:var(--magenta);white-space:nowrap}
.hero-sub{left:562px;top:226px;width:380px;font:600 20px/24px "Montserrat",sans-serif;color:#555}
.hero-sub b{color:var(--magenta)}
.hero-text{left:562px;top:306px;width:420px;font-size:12.5px;color:var(--ink-soft);line-height:1.5}

/* section headings */
.section-title{font:700 21px "Montserrat",sans-serif;color:var(--magenta);padding-bottom:10px;border-bottom:2px solid #ddd;white-space:nowrap}

/* about */
.about-title{left:217px;top:520px}
.about-lead{left:217px;top:562px;width:500px;font:700 23px/27px "Montserrat",sans-serif;color:#555}
.about-lead em{font-style:normal;color:var(--magenta)}
.about-text{left:217px;top:680px;width:510px;font-size:12px;line-height:18px;color:#666}
.btn{background:var(--magenta);color:#fff;font:700 12px "Montserrat",sans-serif;border-radius:4px;display:flex;align-items:center;justify-content:center;gap:8px}
.about-btn{left:217px;top:804px;width:97px;height:35px}
.about-figure{left:735px;top:496px;width:220px;height:378px;background:linear-gradient(180deg,var(--magenta-light),var(--magenta-dark));border-radius:110px 110px 0 0}

/* train */
.train{left:0;top:874px;width:1200px;height:453px;background:var(--band-bg)}
.train-title{left:0;width:1200px;top:920px;text-align:center;font:700 21px "Montserrat",sans-serif;color:var(--magenta)}
.train-rule{left:480px;top:956px;width:240px;height:2px;background:#d6d6d6}
.train-intro{left:180px;width:840px;top:964px;text-align:center;font-size:12.5px;line-height:1.6;color:#666}
.train-figure{left:217px;top:1016px;width:255px;height:255px;border-radius:50%;background:radial-gradient(circle,var(--magenta-light),var(--magenta-dark))}
.train-item{left:489px;width:500px}
.train-item h3{font:700 15px "Montserrat",sans-serif;color:var(--magenta);margin-bottom:8px}
.train-item p{font-size:12.5px;line-height:1.55;color:#666}

/* work from home */
.wfh-title{left:217px;top:1370px;font:700 21px "Montserrat",sans-serif;color:#444;padding-bottom:8px;border-bottom:2px solid #ccc;width:200px;white-space:nowrap}
.wfh-lead{left:217px;top:1418px;width:430px;font:400 17px/24px "Open Sans",sans-serif;color:#555}
.wfh-lead b{color:#333}
.wfh-sub{left:217px;font:700 15px "Montserrat",sans-serif;color:#444}
.wfh-list{left:217px;display:grid;grid-template-columns:150px 150px;column-gap:42px;font-size:12.5px;color:#666}
.wfh-list li{list-style:none;height:26px;line-height:26px;border-bottom:1px solid #e4e4e4}
.wfh-figure{left:657px;top:1365px;width:264px;height:425px;background:linear-gradient(180deg,#666,#333);border-radius:120px 120px 20px 20px}

/* contact */
.contact{left:0;top:1859px;width:1200px;height:432px;background:var(--dark)}
.contact-title{left:0;width:1200px;top:1928px;text-align:center;font:700 21px "Montserrat",sans-serif;color:#fff}
.contact-rule{left:513px;top:1966px;width:176px;height:2px;background:#555}
.field{background:var(--field);border-radius:3px;font-size:11px;color:#777;padding:8px 8px}
.divider{left:701px;top:1995px;width:1px;height:250px;background:var(--line-dark)}
.info h4{font:400 15px "Montserrat",sans-serif;color:#ddd;margin-bottom:14px}
.info p{font-size:13px;color:#888;line-height:1.6}
.info-rule{left:739px;top:2095px;width:245px;height:1px;background:var(--line-dark)}
.send{left:217px;top:2223px;width:90px;height:37px;font-size:15px}

/* footer */
.footer{left:0;top:2291px;width:1200px;height:71px;background:var(--darker);border-top:1px solid var(--line-dark)}
.footer-links{left:217px;top:2320px;font-size:11px;color:#999;display:flex;gap:10px}
.copyright{left:830px;top:2320px;font-size:11px;color:#888}
</style>
</head>
<body>

<div class="abs topbar"></div>
<nav class="abs nav">
  <a class="active">About Us</a><a>Train @ The Parlour Room</a><a>Work from Home</a><a>Contact</a>
</nav>
<div class="abs phone-pill">
  <svg width="13" height="13" viewBox="0 0 24 24"><path fill="#fff" d="M6.6 10.8a15 15 0 0 0 6.6 6.6l2.2-2.2c.3-.3.7-.4 1-.2 1.1.4 2.3.6 3.6.6.6 0 1 .4 1 1V20c0 .6-.4 1-1 1A17 17 0 0 1 3 4c0-.6.4-1 1-1h3.5c.6 0 1 .4 1 1 0 1.3.2 2.5.6 3.6.1.3 0 .7-.2 1z"/></svg>
  555-014-2290
</div>

<section class="abs hero"></section>
<div class="abs hero-logo" role="img" aria-label="Vero Parlour Room mark"><i></i><span>Vero Parlour Room</span></div>
<div class="abs arrow" style="left:136px"><svg width="14" height="14" viewBox="0 0 14 14"><path d="M9 2 4 7l5 5" stroke="#c8157f" stroke-width="2.5" fill="none"/></svg></div>
<div class="abs arrow" style="left:1017px"><svg width="14" height="14" viewBox="0 0 14 14"><path d="m5 2 5 5-5 5" stroke="#c8157f" stroke-width="2.5" fill="none"/></svg></div>
<h1 class="abs hero-title">Welcome the</h1>
<p class="abs hero-sub"><b>Vero Parlour Room</b>, a unique protal into the world of webcam modeling and chat hosting</p>
<p class="abs hero-text">It is a long established fact that a reader will be distracted by the readable content of a page when looking at its layout.</p>

<h2 class="abs section-title about-title">About Us</h2>
<p class="abs about-lead">The Vero Parlour Room was started with the understanding that there is a large number of <em>women who are curious about woeking in webcam</em></p>
<p class="abs about-text">Entertainment, but have no idea where to start. There are hundreds of "studios/ agencies" on the internet with the goal of making money just by getting you to sign up, or even worse, by taking a percentage of your commissions once you do. That is not what The Parlour Room is about. We want to be the premier destination for webcam entertainers to further their careers, no matter what to be the premier destination you have....</p>
<div class="abs btn about-btn">Read More</div>
<div class="abs about-figure" role="img" aria-label="Magenta silhouette of a standing woman"></div>

<section class="abs train"></section>
<h2 class="abs train-title">Train @ Vero Parlour Room</h2>
<div class="abs train-rule"></div>
<p class="abs train-intro">It is a long established fact that a reader will be distracted by the readable content of a page when looking at its layout.<br>The point of using Lorem Ipsum is that it has a more-or-less normal distribution</p>
<div class="abs train-figure" role="img" aria-label="Emblem with silhouettes of three women in a circle"></div>
<div class="abs train-item" style="top:1040px">
  <h3>Many desktop publishing</h3>
  <p>It is a long established fact that a reader will be distracted by the readable content of a page when looking at its layout. The point of using Lorem Ipsum is that it has a more-or-less normal distribution of letters, as opposed to using 'Content here, content here', making it look like readable English. Many desktop publishing.</p>
</div>
<div class="abs train-item" style="top:1156px">
  <h3>Many desktop publishing</h3>
  <p>It is a long established fact that a reader will be distracted by the readable content of a page when looking at its layout. The point of using Lorem Ipsum is that it has a more-or-less normal distribution of letters, as opposed to using 'Content here, content here', making it look like readable English. Many desktop publishing...</p>
</div>

<h2 class="abs wfh-title">Work from Home</h2>
<p class="abs wfh-lead">Working as a webcam entertainer can be a <b>very lucrative business, whether it is your only job or something</b> you do on the side. <b>It gives you the flexibility to create</b> your own schedule based around your availability</p>
<h3 class="abs wfh-sub" style="top:1554px">What do I need?</h3>
<ul class="abs wfh-list" style="top:1578px">
  <li>Working as a webcam</li><li>Working as a webcam</li>
  <li>Very lucrative business</li><li>Very lucrative business</li>
  <li>There are hundreds</li><li>There are hundreds</li>
</ul>
<h3 class="abs wfh-sub" style="top:1674px">How do I sign up ?</h3>
<ul class="abs wfh-list" style="top:1696px">
  <li>Working as a webcam</li><li>Working as a webcam</li>
  <li>Very lucrative business</li><li>Very lucrative business</li>
  <li>There are hundreds</li><li>There are hundreds</li>
</ul>
<div class="abs wfh-figure" role="img" aria-label="Grey silhouette of a woman seated on a chair"></div>

<section class="abs contact"></section>
<h2 class="abs contact-title">Contact</h2>
<div class="abs contact-rule"></div>
<div class="abs field" style="left:217px;top:2017px;width:220px;height:31px">First Name*</div>
<div class="abs field" style="left:449px;top:2017px;width:219px;height:31px">Email*</div>
<div class="abs field" style="left:217px;top:2059px;width:220px;height:31px">Contact Phone No*</div>
<div class="abs field" style="left:449px;top:2059px;width:219px;height:31px">Subject*</div>
<div class="abs field" style="left:217px;top:2100px;width:451px;height:101px">Message*</div>
<div class="abs btn send">SEND
  <svg width="14" height="14" viewBox="0 0 24 24"><path fill="#fff" d="M2 21 23 12 2 3v7l15 2-15 2z"/></svg>
</div>
<div class="abs divider"></div>
<div class="abs info" style="left:739px;top:2002px">
  <h4>Location</h4>
  <p>It is a long established fact that<br>a reader will be distracted</p>
</div>
<div class="abs info-rule"></div>
<div class="abs info" style="left:739px;top:2122px">
  <h4>Contact</h4>
  <p>Phone : 555-014-2290<br>Email : hello@veroparlourroom.example</p>
</div>

<footer class="abs footer"></footer>
<div class="abs footer-links"><span>About Us</span><span>|</span><span>Train @ The Parlour Room</span><span>|</span><span>Work from Home</span><span>|</span><span>Contact</span></div>
<div class="abs copyright">Copyright © 2016 Vero Parlour Room</div>

</body>
</html>
```